詳しくは依頼図をご確認下さい。

紙はクラフトの厚口、もしくは色上質の厚口薄茶やオレンジなど珈琲と相性のいい色を想定しています。 ※白インクが使えます。

コンビニみたいなところで販売しているカップコーヒーのチケットです。
喫茶店ではありません。

全体の長さはお任せしますがあまり長すぎるのもおかしいのかなと思います。

裏はスタンプを押すので空欄で考えています。

白インクまたは透明インクを使った複製防止案があれば
遠慮無く盛り込んでください。

下からもぎっていきます。短くなっていくにつれて楽しみのあるデザインもしくはフレーズ、その他アイデアがあると◎

ミシン目、穴のある想定でお願いします。
各チケットに、お店の店名や会社名(マーク)が入ります。
横長の長方形でいいです。その分のスペースを空けてください。
※マークは後からこちらで入れます

白インク、透明インクが使えますと書きましたが、
使わなければいけないということではありません。
なかなか表現がしにくいので、無くても大丈夫です。
※必要ならこちらで後から入れます
裏面白紙という表現がございましたが
裏面には「なにも印刷しない」という意味です。
ですので白い紙、ということではありません。
わかりにくくて申し訳ございませんでした。

単純に素晴らしいデザインセンスだったからです。こちらの要望を全て形にしていただきました。対応も迅速でしたし、相談したら提案もしてくださいました。

皆さんのデザインも感激するものばかりでした。遅くなってしまいましたが、ご厚意に感謝いたします。

```html
<!DOCTYPE html>
<html lang="ja">
<head>
<meta charset="utf-8">
<title>Coffee Ticket Strip</title>
<link rel="stylesheet" href="https://fonts.googleapis.com/css2?family=Playfair+Display:wght@400;700&family=Oswald:wght@500&family=Noto+Sans+JP:wght@400&display=swap">
<style>
  :root {
    --kraft: #c99a5c;
    --ink-brown: #8a5a22;
    --ink-white: #f6ead6;
    --perforation: #9c6e37;
    --logo-line: rgba(246,234,214,0.75);
    --page: #ffffff;
  }
  * { margin: 0; padding: 0; box-sizing: border-box; }
  html, body { width: 849px; height: 1200px; overflow: hidden; background: var(--page); }
  .canvas { position: relative; width: 849px; height: 1200px; }
  .hole-label {
    position: absolute; left: 414px; top: 4px; width: 22px; text-align: center;
    font: 400 14px "Noto Sans JP", sans-serif; color: #555;
  }
  .strip {
    position: absolute; left: 305px; top: 26px; width: 238px; height: 1106px;
    background: var(--kraft);
    display: flex; flex-direction: column;
    overflow: hidden;
  }
  .art-area {
    position: absolute; left: 96px; top: 40px; width: 70px; height: 1060px;
    background: linear-gradient(180deg, rgba(246,234,214,0.10), rgba(246,234,214,0.28));
  }
  .header { position: relative; height: 82px; }
  .hole {
    position: absolute; left: 111px; top: 8px; width: 14px; height: 14px;
    border-radius: 50%; background: var(--page); border: 1px solid var(--perforation);
  }
  .notice {
    position: absolute; left: 16px; top: 46px;
    font: 500 7px/9.5px "Oswald", sans-serif; color: var(--ink-white); letter-spacing: 0.3px;
  }
  .ticket {
    position: relative; height: 85.33px;
    border-top: 2px dashed var(--perforation);
    display: flex; align-items: center; justify-content: space-between;
    padding: 0 18px 0 14px;
  }
  .ticket-info { position: relative; display: flex; flex-direction: column; gap: 6px; }
  .ticket-label {
    font: 700 17px/18px "Playfair Display", serif; color: var(--ink-white);
    letter-spacing: 0.5px;
  }
  .logo-space {
    width: 96px; height: 16px;
    border: 1px dashed var(--logo-line);
  }
  .ticket-number {
    position: relative;
    font: 400 46px/1 "Playfair Display", serif; color: var(--ink-brown);
    transform: scaleX(0.82); transform-origin: right center;
  }
</style>
</head>
<body>
<div class="canvas">
  <div class="hole-label">穴</div>
  <div class="strip">
    <div class="art-area" role="img" aria-label="Faint white illustration of stacked coffee cups running down the strip"></div>
    <div class="header">
      <div class="hole"></div>
      <p class="notice">Tear from the bottom<br>One cup per ticket<br>Keep this strip</p>
    </div>
    <div class="ticket"><div class="ticket-info"><p class="ticket-label">COFFEE<br>TICKET</p><div class="logo-space"></div></div><span class="ticket-number">1</span></div>
    <div class="ticket"><div class="ticket-info"><p class="ticket-label">COFFEE<br>TICKET</p><div class="logo-space"></div></div><span class="ticket-number">2</span></div>
    <div class="ticket"><div class="ticket-info"><p class="ticket-label">COFFEE<br>TICKET</p><div class="logo-space"></div></div><span class="ticket-number">3</span></div>
    <div class="ticket"><div class="ticket-info"><p class="ticket-label">COFFEE<br>TICKET</p><div class="logo-space"></div></div><span class="ticket-number">4</span></div>
    <div class="ticket"><div class="ticket-info"><p class="ticket-label">COFFEE<br>TICKET</p><div class="logo-space"></div></div><span class="ticket-number">5</span></div>
    <div class="ticket"><div class="ticket-info"><p class="ticket-label">COFFEE<br>TICKET</p><div class="logo-space"></div></div><span class="ticket-number">6</span></div>
    <div class="ticket"><div class="ticket-info"><p class="ticket-label">COFFEE<br>TICKET</p><div class="logo-space"></div></div><span class="ticket-number">7</span></div>
    <div class="ticket"><div class="ticket-info"><p class="ticket-label">COFFEE<br>TICKET</p><div class="logo-space"></div></div><span class="ticket-number">8</span></div>
    <div class="ticket"><div class="ticket-info"><p class="ticket-label">COFFEE<br>TICKET</p><div class="logo-space"></div></div><span class="ticket-number">9</span></div>
    <div class="ticket"><div class="ticket-info"><p class="ticket-label">COFFEE<br>TICKET</p><div class="logo-space"></div></div><span class="ticket-number">10</span></div>
    <div class="ticket"><div class="ticket-info"><p class="ticket-label">COFFEE<br>TICKET</p><div class="logo-space"></div></div><span class="ticket-number">11</span></div>
    <div class="ticket"><div class="ticket-info"><p class="ticket-label">COFFEE<br>TICKET</p><div class="logo-space"></div></div><span class="ticket-number">12</span></div>
  </div>
</div>
</body>
</html>
```